Waterproofing Construction company needs letterhead

I need a letterhead design for a commercial waterproofing construction company. We would like to see designs that are contemporary, clean, sleek and use our logo. Our current design is dated. I would also like a cover page (see example) that goes with our letterhead. I would like for the footer to have our address, website, and phone number

Target Market(s)

Customers, potential customers.

Font styles to use
Sans Serif

Requirements
Must have
• logo, website, address, phone numbers, only our colors, tahoma font
• PMS: 295C PMS: 2995C
• CMYK: 100/84/36/39 CMYK: 80/12/1/0
• RGB: 16/44/82 RGB: 0/167/224
• HEX#: #102C52 HEX#: #00A7E0
• Black & White: 100% Black & White: 32%
• Gray Scale: 90% Gray Scale: 32%
Nice to have
• Our "icon" logo attached would be nice somewhere on the page.

```html
<!DOCTYPE html>
<html lang="en">
<head>
<meta charset="utf-8">
<title>NRV Letterhead</title>
<link href="https://fonts.googleapis.com/css2?family=Noto+Sans:wght@400;700;800&display=swap" rel="stylesheet">
<style>
  :root {
    --navy: #1f2f52;
    --sky: #5aa7e0;
    --paper: #ffffff;
  }
  html, body {
    margin: 0;
    padding: 0;
    overflow: hidden;
    background: var(--paper);
  }
  .letterhead {
    position: relative;
    width: 849px;
    height: 1200px;
    overflow: hidden;
    background: var(--paper);
    font-family: "Noto Sans", Tahoma, sans-serif;
  }
  .header-band,
  .corner-accent {
    position: absolute;
    display: block;
  }
  .header-band { left: 0; top: 0; }
  .corner-accent { left: 760px; top: 1060px; z-index: 2; }
  .brand {
    position: absolute;
    left: 580px;
    top: 52px;
    display: flex;
    align-items: center;
    gap: 8px;
  }
  .brand-name {
    font-size: 86px;
    font-weight: 800;
    line-height: 1;
    letter-spacing: -3px;
    color: var(--navy);
  }
  .brand-mark {
    width: 22px;
    height: 22px;
    background: var(--sky);
    margin-top: 34px;
  }
  .footer {
    position: absolute;
    left: 0;
    bottom: 0;
    width: 849px;
    height: 84px;
    background: var(--navy);
    color: var(--paper);
  }
  .footer-phones {
    position: absolute;
    left: 30px;
    top: 16px;
    font-size: 19px;
    line-height: 24px;
    letter-spacing: 3.6px;
    white-space: nowrap;
  }
  .footer-web {
    position: absolute;
    left: 297px;
    top: 26px;
    font-size: 19px;
    font-weight: 700;
    letter-spacing: 6px;
    white-space: nowrap;
  }
  .footer-address {
    position: absolute;
    left: 583px;
    width: 200px;
    top: 16px;
    text-align: center;
    font-size: 18px;
    line-height: 21px;
    letter-spacing: 3.6px;
    white-space: nowrap;
  }
</style>
</head>
<body>
<div class="letterhead">
  <svg class="header-band" width="528" height="137" viewBox="0 0 528 137" role="img" aria-label="Header band with diagonal stripe texture">
    <defs>
      <linearGradient id="band-fade" x1="0" y1="0" x2="1" y2="0">
        <stop offset="0" stop-color="#3a6aa3"/>
        <stop offset="0.45" stop-color="#1f2f52"/>
        <stop offset="1" stop-color="#1f2f52"/>
      </linearGradient>
    </defs>
    <polygon points="0,0 528,0 439,137 0,137" fill="url(#band-fade)"/>
  </svg>

  <div class="brand">
    <span class="brand-name">NRV</span>
    <span class="brand-mark"></span>
  </div>

  <footer class="footer">
    <div class="footer-phones">
      <div>O: (877) 555-0182</div>
      <div>F: (919) 555-0147</div>
    </div>
    <div class="footer-web">www.NRVwp.com</div>
    <div class="footer-address">
      <div>PO Box 416</div>
      <div>Cary, NC 27513</div>
    </div>
  </footer>

  <svg class="corner-accent" width="89" height="140" viewBox="0 0 89 140" role="img" aria-label="Corner diagonal stripe texture">
    <defs>
      <linearGradient id="corner-fade" x1="0" y1="1" x2="1" y2="0">
        <stop offset="0" stop-color="#5aa7e0" stop-opacity="0.55"/>
        <stop offset="1" stop-color="#5aa7e0" stop-opacity="0.15"/>
      </linearGradient>
    </defs>
    <polygon points="18,140 89,0 89,140" fill="url(#corner-fade)"/>
  </svg>
</div>
</body>
</html>
```